Loyalty card for customers

I would like logo an a section for 10 places, so I can advertise 10th float is free, our business is health and wellness we offer magnesium float, hyperbaric oxygen and infrared sauna

```html
<!DOCTYPE html>
<html lang="en">
<head>
<meta charset="utf-8">
<title>Still Tide Loyalty Card</title>
<link rel="stylesheet" href="https://fonts.googleapis.com/css2?family=Nunito:wght@800;900&display=swap">
<style>
  :root {
    --page-bg: #ffffff;
    --brand-blue: #2a9fd6;
    --deep-blue: #1c5fb3;
    --stamp-ring: #2f6fc4;
    --stamp-fill: #ffffff;
    --peach: #f7d6ad;
    --sand: #f3c36e;
    --mist: #eef0f7;
    --lavender: #dcdff0;
    --aqua: #8fdbe0;
    --lagoon: #5cc6d8;
  }
  * { box-sizing: border-box; margin: 0; padding: 0; }
  html, body {
    width: 1200px;
    height: 1200px;
    overflow: hidden;
    background: var(--page-bg);
  }
  .canvas {
    position: relative;
    width: 1200px;
    height: 1200px;
  }
  .loyalty-card {
    position: absolute;
    left: 100px;
    top: 317px;
    width: 1000px;
    height: 565px;
    overflow: hidden;
    font-family: "Nunito", sans-serif;
  }
  .card-art {
    position: absolute;
    inset: 0;
    width: 100%;
    height: 100%;
  }
  .brand-name {
    position: absolute;
    top: 70px;
    left: 0;
    width: 100%;
    text-align: center;
    font-size: 108px;
    font-weight: 900;
    letter-spacing: 10px;
    color: var(--brand-blue);
    line-height: 1.2;
  }
  .offer-headline {
    position: absolute;
    top: 338px;
    left: 0;
    width: 100%;
    text-align: center;
    font-size: 46px;
    font-weight: 900;
    color: #ffffff;
    text-shadow:
      2px 0 0 var(--deep-blue), -2px 0 0 var(--deep-blue),
      0 2px 0 var(--deep-blue), 0 -2px 0 var(--deep-blue),
      2px 2px 0 var(--deep-blue), -2px -2px 0 var(--deep-blue),
      2px -2px 0 var(--deep-blue), -2px 2px 0 var(--deep-blue);
  }
  .stamp-row {
    position: absolute;
    top: 462px;
    left: 53px;
    display: flex;
    gap: 38px;
    list-style: none;
  }
  .stamp {
    width: 56px;
    height: 56px;
    border-radius: 50%;
    background: var(--stamp-fill);
    border: 3px solid var(--stamp-ring);
    box-shadow: inset 0 0 0 3px var(--stamp-fill), inset 0 0 0 5px var(--stamp-ring);
    display: flex;
    align-items: center;
    justify-content: center;
    font-size: 30px;
    font-weight: 800;
    color: var(--stamp-ring);
  }
  .stamp-free {
    font-size: 13px;
    font-weight: 900;
  }
</style>
</head>
<body>
<main class="canvas">
  <section class="loyalty-card">
    <svg class="card-art" viewBox="0 0 1000 565" role="img" aria-label="Soft watercolour wash in peach, sand, white and lagoon blue">
      <defs>
        <linearGradient id="top-wash" x1="0" y1="0" x2="1" y2="0">
          <stop offset="0" stop-color="var(--peach)"/>
          <stop offset="0.45" stop-color="var(--mist)"/>
          <stop offset="1" stop-color="var(--lavender)"/>
        </linearGradient>
        <linearGradient id="bottom-wash" x1="0" y1="0" x2="1" y2="0">
          <stop offset="0" stop-color="var(--sand)"/>
          <stop offset="0.22" stop-color="#f5e2bd"/>
          <stop offset="0.42" stop-color="#f4f6fa"/>
          <stop offset="0.7" stop-color="var(--aqua)"/>
          <stop offset="1" stop-color="var(--lagoon)"/>
        </linearGradient>
      </defs>
      <rect width="1000" height="565" fill="url(#top-wash)"/>
      <path d="M0 240 Q500 300 1000 240 L1000 565 L0 565 Z" fill="url(#bottom-wash)"/>
      <path d="M0 240 Q500 300 1000 240" fill="none" stroke="#ffffff" stroke-width="6"/>
    </svg>
    <h1 class="brand-name">Still Tide</h1>
    <p class="offer-headline">Buy 9, 10th Float is Free</p>
    <ol class="stamp-row">
      <li class="stamp">1</li>
      <li class="stamp">2</li>
      <li class="stamp">3</li>
      <li class="stamp">4</li>
      <li class="stamp">5</li>
      <li class="stamp">6</li>
      <li class="stamp">7</li>
      <li class="stamp">8</li>
      <li class="stamp">9</li>
      <li class="stamp stamp-free">FREE</li>
    </ol>
  </section>
</main>
</body>
</html>
```